Typographic word art illustration of life lessons

I've written out all the meaningful life lessons my parents have taught me and would like to give it to them for Christmas in the form of a typographic word art design. This will be a print project. I'd like the size of the design to be no larger than 11x17, no smaller than 8.5x11.
The text must be readable in the complete sentences provided.
The text can be displayed in multiple directions, as long as each sentence is readable.
The text itself should be arranged in an artistic and creative way. I'm not looking for text that is aligned in normal-looking rows with a an image watermark behind it.
Sentences may be included on the same row if it works with the design.
Font, Case and Text may be alternated to best suite your design. No grunge fonts, or small-size handwriting fonts, or anything that is difficult to read.
Text could fit into a shape or silhouette (ie: heart, tree, or anything that symbolizes family, life, love, etc.), or form an abstract design, or it can be justified to fit the whole page.
I'm not looking for anything super colorful. Black and white would work, or any standard color palette. The intended result is something they can hang on their wall.
Text is attached in a pdf. Minor tweaks to text is ok if necessary for formatting design, but in general, text should remain unedited.
I've also added some examples of the type of word art I had in mind.
Please help me make this gift into something beautiful and special!
Updates
I trimmed the text down significantly because all the designs seemed to crowded, and had to use fonts that were too small. Here is the revised text:
Don’t give up until you’ve given your all.
Don’t let people that hurt you occupy your mind.
Good people do bad things. Get over it.
Block bitterness from ever taking root in your heart.
Take every opportunity to express gratitude.
True brotherhood is forged out of loyalty and love.
There is no excuse for deceit.
Words matter.
Forgiveness is not optional.
Never make insincere apologies.
Worrying is a waste of time.
Choose your destiny by choosing your friends.
Marriage is a unified front. Make your spouse a priority.
Truth and grace are inseparable.
Humor disarms, softens and endears.
Selflessness is a lifestyle.
Whenever possible, give generously and anonymously.
Never apologize and give an excuse in the same sentence.
Faith must fuel the core of who you are.
The path to freedom begins with asking difficult questions.
Take advantage of every opportunity to educate yourself.
Be your spouse’s protector and advocate.
Radiate humility, vulnerability and love.
Give your finish line the ability to expand.

```html
<!DOCTYPE html>
<html lang="en">
<head>
<meta charset="utf-8">
<title>Life Lessons – Typographic Heart</title>
<link rel="stylesheet" href="https://fonts.googleapis.com/css2?family=Montserrat:wght@300;400;700;800&family=Oswald:wght@500;700&family=Lobster+Two:ital,wght@1,700&display=swap">
<style>
  :root {
    --page: #e8ebeb;
    --ink: #1f212d;
    --teal: #62c6b1;
    --pink: #c67bbd;
  }
  html, body {
    margin: 0;
    width: 1200px;
    height: 1000px;
    overflow: hidden;
    background: var(--page);
  }
  .poster {
    position: absolute;
    left: 26px;
    top: 90px;
    width: 1148px;
    height: 819px;
    display: block;
  }
  .card { fill: var(--ink); }
  .frame-outer { fill: none; stroke: var(--pink); stroke-width: 4; }
  .frame-inner { fill: none; stroke: var(--teal); stroke-width: 1.5; }
  .teal { fill: var(--teal); }
  .pink { fill: var(--pink); }
  .ink { fill: var(--ink); }
  .sans-black { font-family: "Montserrat", sans-serif; font-weight: 800; }
  .sans-bold { font-family: "Montserrat", sans-serif; font-weight: 700; }
  .sans-light { font-family: "Montserrat", sans-serif; font-weight: 300; }
  .sans { font-family: "Montserrat", sans-serif; font-weight: 400; }
  .condensed { font-family: "Oswald", sans-serif; font-weight: 700; }
  .script { font-family: "Lobster Two", cursive; font-style: italic; font-weight: 700; }
  .spaced { letter-spacing: 2px; }
</style>
</head>
<body>
<svg class="poster" viewBox="122 158 956 682" xmlns="http://www.w3.org/2000/svg" aria-label="Life lessons arranged in the shape of a heart">
  <!-- card and frame -->
  <rect class="card" x="122" y="158" width="956" height="682"/>
  <path class="frame-outer" d="M182,195 H1018 A22,22 0 0 0 1040,217 V783 A22,22 0 0 0 1018,805 H182 A22,22 0 0 0 160,783 V217 A22,22 0 0 0 182,195 Z"/>
  <path class="frame-inner" d="M203,208 H997 A30,30 0 0 0 1027,238 V762 A30,30 0 0 0 997,792 H203 A30,30 0 0 0 173,762 V238 A30,30 0 0 0 203,208 Z"/>

  <!-- decorative placeholders -->
  <rect class="teal" x="395" y="292" width="36" height="36" rx="14" role="img" aria-label="Small bird ornament"/>
  <rect class="teal" x="487" y="264" width="20" height="16" rx="3" role="img" aria-label="Small crown ornament"/>
  <circle class="pink" cx="359" cy="380" r="16" role="img" aria-label="Snowflake ornament"/>
  <ellipse class="pink" cx="697" cy="278" rx="33" ry="19" role="img" aria-label="Cloud ornament"/>
  <rect class="teal" x="571" y="316" width="52" height="14" rx="7" role="img" aria-label="Flourish ornament"/>
  <ellipse class="pink" cx="857" cy="402" rx="9" ry="13" role="img" aria-label="Flame ornament"/>

  <!-- simple icons -->
  <polygon class="teal" points="872,426 874.5,431 880,431.5 876,435 877.5,440.5 872,437.5 866.5,440.5 868,435 864,431.5 869.5,431"/>
  <path class="teal" d="M598,728 L591,721 A4,4 0 0 1 598,716 A4,4 0 0 1 605,721 Z"/>
  <circle class="pink" cx="493" cy="667" r="7"/>
  <rect class="pink" x="622" y="640" width="28" height="28"/>
  <polygon class="ink" points="636,644 639,651 646,651.5 641,656 642.5,663 636,659.5 629.5,663 631,656 626,651.5 633,651"/>

  <!-- LEFT LOBE -->
  <text class="script pink" x="487" y="296" font-size="11" text-anchor="middle">Whenever possible</text>
  <text class="script pink" x="487" y="312" font-size="17" text-anchor="middle"><tspan font-size="11">give </tspan>generously</text>
  <text class="script pink" x="495" y="330" font-size="17" text-anchor="middle"><tspan font-size="11">and </tspan>anonymously</text>

  <text class="sans-black teal" x="383" y="362" font-size="36" textLength="214" lengthAdjust="spacingAndGlyphs">MARRIAGE</text>
  <text class="sans-black teal" x="383" y="381" font-size="13" textLength="214" lengthAdjust="spacingAndGlyphs">IS A UNIFIED FRONT MAKE</text>
  <text class="sans-black teal" x="383" y="398" font-size="13" textLength="214" lengthAdjust="spacingAndGlyphs">YOUR SPOUSE A PRIORITY</text>

  <text class="sans teal" x="333" y="418" font-size="17" textLength="249" lengthAdjust="spacingAndGlyphs">SELFLESSNESS <tspan class="pink" font-size="10">is a </tspan>LIFESTYLE</text>

  <text class="sans-bold teal" x="316" y="435" font-size="9.5" textLength="116" lengthAdjust="spacingAndGlyphs">SHOW YOUR CHILDREN:</text>
  <text class="script teal" x="316" y="447" font-size="10.5" textLength="116" lengthAdjust="spacingAndGlyphs">humility, vulnerability &amp; love</text>
  <text class="sans teal" x="316" y="458" font-size="7.5" textLength="116" lengthAdjust="spacingAndGlyphs">FRIENDS MAY COME AND GO BUT</text>
  <text class="sans teal" x="366" y="467" font-size="7.5" textLength="66" lengthAdjust="spacingAndGlyphs">NEVER CHANGES</text>
  <text class="condensed teal" x="316" y="479" font-size="20" textLength="44" lengthAdjust="spacingAndGlyphs">FAMILY</text>
  <text class="script teal" x="362" y="487" font-size="23" textLength="110" lengthAdjust="spacingAndGlyphs">Freedom</text>
  <text class="sans teal" x="320" y="491" font-size="8" textLength="40" lengthAdjust="spacingAndGlyphs">THE PATH TO</text>
  <text class="sans teal" x="320" y="505" font-size="8.5" textLength="152" lengthAdjust="spacingAndGlyphs">BEGINS WITH ASKING DIFFICULT</text>
  <text class="sans-bold teal" x="328" y="521" font-size="9" textLength="252" lengthAdjust="spacingAndGlyphs">GIVE YOUR FINISH LINE THE ABILITY TO EXPAND</text>

  <text class="sans-bold pink" font-size="9" transform="translate(476,479) rotate(-90)" textLength="34" lengthAdjust="spacingAndGlyphs">DON’T</text>
  <text class="sans-bold teal" x="479" y="430" font-size="8.5" textLength="103" lengthAdjust="spacingAndGlyphs">LET PEOPLE THAT HURT</text>
  <text class="sans-bold teal" x="479" y="442" font-size="8.5" textLength="103" lengthAdjust="spacingAndGlyphs">YOU OCCUPY YOUR</text>
  <text class="condensed pink" x="479" y="477" font-size="40" textLength="103" lengthAdjust="spacingAndGlyphs">MIND</text>
  <text class="script teal" x="476" y="498" font-size="22" textLength="104" lengthAdjust="spacingAndGlyphs">Questions</text>

  <!-- people in need column -->
  <text class="sans-bold teal" x="326" y="536" font-size="10" textLength="40" lengthAdjust="spacingAndGlyphs">PEOPLE</text>
  <text class="sans-bold teal" x="326" y="549" font-size="10" textLength="44" lengthAdjust="spacingAndGlyphs">IN NEED</text>
  <text class="sans teal" x="334" y="560" font-size="6.5" textLength="36" lengthAdjust="spacingAndGlyphs">SHOULDN’T</text>
  <text class="sans teal" x="342" y="570" font-size="6.5" textLength="28" lengthAdjust="spacingAndGlyphs">NEED TO</text>
  <text class="sans teal" x="344" y="580" font-size="6.5" textLength="28" lengthAdjust="spacingAndGlyphs">ASK FOR</text>
  <text class="sans-bold teal" x="348" y="593" font-size="11" textLength="30" lengthAdjust="spacingAndGlyphs">YOUR</text>
  <text class="sans-bold teal" x="352" y="606" font-size="11" textLength="26" lengthAdjust="spacingAndGlyphs">SELF</text>

  <text class="sans-light pink" x="389" y="532" font-size="9.5" textLength="193" lengthAdjust="spacingAndGlyphs">THE ONLY THING THAT MATTERS MORE</text>
  <text class="sans-light pink" x="389" y="544" font-size="9.5" textLength="193" lengthAdjust="spacingAndGlyphs">THAN YOUR REPUTATION IS YOUR</text>
  <text class="sans-black pink" x="380" y="572" font-size="27" textLength="202" lengthAdjust="spacingAndGlyphs">CHARACTER</text>

  <text class="script teal" x="389" y="588" font-size="16">Faith</text>
  <text class="sans-bold teal" x="432" y="587" font-size="10.5" textLength="150" lengthAdjust="spacingAndGlyphs">MUST FUEL THE CORE OF</text>
  <text class="sans-bold pink" x="391" y="601" font-size="7.5" textLength="84" lengthAdjust="spacingAndGlyphs">BE YOUR SPOUSE’S</text>
  <text class="script teal" x="480" y="603" font-size="17" textLength="100" lengthAdjust="spacingAndGlyphs">who you are</text>
  <text class="sans-bold pink" x="390" y="619" font-size="12.5" textLength="191" lengthAdjust="spacingAndGlyphs">PROTECTOR &amp; ADVOCATE</text>

  <text class="sans-black teal" x="415" y="638" font-size="18" textLength="197" lengthAdjust="spacingAndGlyphs">HUMOR DISARMS,</text>
  <text class="sans-black teal" x="452" y="658" font-size="18" textLength="160" lengthAdjust="spacingAndGlyphs">SOFTENS AND</text>
  <text class="sans-black teal" x="504" y="677" font-size="18" textLength="104" lengthAdjust="spacingAndGlyphs">ENDEARS</text>

  <text class="sans teal" x="593" y="689" font-size="9.5" text-anchor="middle">NEVER APOLOGIZE &amp; GIVE</text>
  <text class="sans teal" x="593" y="701" font-size="9.5" text-anchor="middle">EXCUSE IN THE SAME</text>
  <text class="sans teal" x="593" y="713" font-size="9.5" text-anchor="middle">SENTENCE</text>

  <!-- CENTRE SPINE -->
  <text class="condensed teal" font-size="30" transform="translate(610,616) rotate(-90)" textLength="218" lengthAdjust="spacingAndGlyphs">WORDS<tspan class="pink">MATTER</tspan></text>
  <text class="script pink" font-size="13" transform="translate(626,622) rotate(-90)" textLength="146" lengthAdjust="spacingAndGlyphs">Worrying is a waste of time</text>
  <text class="condensed teal" font-size="22" transform="translate(627,476) rotate(90)" textLength="150" lengthAdjust="spacingAndGlyphs">GET OVER IT</text>
  <text class="sans-bold pink" font-size="8" transform="translate(651,476) rotate(90)" textLength="150" lengthAdjust="spacingAndGlyphs">GOOD PEOPLE DO BAD THINGS</text>

  <!-- RIGHT LOBE -->
  <text class="sans-black teal" x="632" y="316" font-size="17" textLength="142" lengthAdjust="spacingAndGlyphs">NEVER MAKE</text>
  <text class="sans-bold teal" x="632" y="332" font-size="11.5" textLength="146" lengthAdjust="spacingAndGlyphs">INSINCERE APOLOGIES</text>
  <text class="sans teal" x="614" y="352" font-size="11.5" textLength="176" lengthAdjust="spacingAndGlyphs">THE ONLY STANDARD WORTH</text>
  <text class="sans teal" x="614" y="365" font-size="11.5" textLength="216" lengthAdjust="spacingAndGlyphs">STRIVING FOR IS YOUR OWN FULL</text>
  <text class="sans-black teal" x="612" y="398" font-size="36" textLength="228" lengthAdjust="spacingAndGlyphs">POTENTIAL</text>

  <text class="sans teal" x="612" y="411" font-size="10" textLength="236" lengthAdjust="spacingAndGlyphs">YOU DON’T HAVE THE RIGHT TO JUDGE,</text>
  <text class="sans teal" x="612" y="424" font-size="10" textLength="178" lengthAdjust="spacingAndGlyphs">BUT YOU HAVE THE CHOICE TO</text>
  <text class="script pink" x="797" y="439" font-size="28" textLength="62" lengthAdjust="spacingAndGlyphs">Help</text>
  <text class="sans-bold teal" x="612" y="437" font-size="9" textLength="170" lengthAdjust="spacingAndGlyphs">FORGIVENESS <tspan class="script pink">is not</tspan> OPTIONAL</text>

  <text class="script teal" x="610" y="462" font-size="26" textLength="153" lengthAdjust="spacingAndGlyphs">Truth <tspan class="pink" font-size="18">&amp;</tspan> Grace</text>
  <text class="sans teal" x="780" y="453" font-size="7" textLength="88" lengthAdjust="spacingAndGlyphs">DON’T GIVE UP UNTIL</text>
  <text class="sans teal" x="780" y="464" font-size="7" textLength="88" lengthAdjust="spacingAndGlyphs">YOU’VE GIVEN YOUR</text>
  <text class="sans-bold teal" font-size="8" transform="translate(880,466) rotate(-90)" textLength="17" lengthAdjust="spacingAndGlyphs">ALL</text>

  <text class="script pink" x="660" y="478" font-size="15" textLength="90" lengthAdjust="spacingAndGlyphs">are inseparable</text>
  <text class="sans-bold pink" x="680" y="490" font-size="9.5" textLength="70" lengthAdjust="spacingAndGlyphs">CHOOSE YOUR</text>
  <text class="sans-bold pink" x="660" y="501" font-size="9.5" textLength="90" lengthAdjust="spacingAndGlyphs">BY CHOOSING YOUR</text>
  <text class="condensed pink" x="754" y="490" font-size="28" textLength="128" lengthAdjust="spacingAndGlyphs">DESTINY</text>
  <text class="condensed pink" x="754" y="517" font-size="28" textLength="128" lengthAdjust="spacingAndGlyphs">FRIENDS</text>

  <text class="sans-light teal spaced" x="660" y="517" font-size="10" textLength="88" lengthAdjust="spacingAndGlyphs">TAKE EVERY</text>
  <text class="script teal" x="660" y="534" font-size="20" textLength="88" lengthAdjust="spacingAndGlyphs">Opportunity</text>
  <text class="sans-light teal spaced" x="668" y="549" font-size="10" textLength="78" lengthAdjust="spacingAndGlyphs">TO EXPRESS</text>
  <text class="script teal" x="750" y="549" font-size="18" textLength="78" lengthAdjust="spacingAndGlyphs">Gratitude</text>
  <text class="sans teal" x="772" y="526" font-size="7.5" textLength="108" lengthAdjust="spacingAndGlyphs">BLOCK BITTERNESS FROM</text>
  <text class="sans teal" x="772" y="536" font-size="7.5" textLength="108" lengthAdjust="spacingAndGlyphs">EVER TAKING ROOT IN YOUR</text>
  <text class="sans-light pink" x="834" y="550" font-size="15" textLength="46" lengthAdjust="spacingAndGlyphs">HEART</text>

  <text class="sans-bold teal" x="660" y="563" font-size="9.5" textLength="196" lengthAdjust="spacingAndGlyphs">TRUE BROTHERHOOD IS FORGED OUT OF</text>
  <text class="sans-black teal" x="660" y="587" font-size="24" textLength="196" lengthAdjust="spacingAndGlyphs">LOYALTY<tspan class="pink">&amp;</tspan>LOVE</text>
  <text class="script teal" x="660" y="603" font-size="12" textLength="180" lengthAdjust="spacingAndGlyphs">There is no <tspan class="sans-bold" font-style="normal">EXCUSE</tspan> <tspan class="pink">for</tspan> <tspan class="sans-bold" font-style="normal">DECEIT</tspan></text>
  <text class="sans teal" x="660" y="615" font-size="9" textLength="128" lengthAdjust="spacingAndGlyphs">STAND UP FOR THOSE WHO CAN’T</text>
  <text class="sans teal" x="660" y="628" font-size="9" textLength="55" lengthAdjust="spacingAndGlyphs">STAND UP FOR</text>
  <text class="script pink" x="718" y="630" font-size="20" textLength="102" lengthAdjust="spacingAndGlyphs">themselves</text>

  <text class="sans teal" x="660" y="646" font-size="8" textLength="96" lengthAdjust="spacingAndGlyphs">WILLPOWER CAN EMPOWER</text>
  <text class="sans teal" x="660" y="657" font-size="8" textLength="96" lengthAdjust="spacingAndGlyphs">YOU TO ACCOMPLISH</text>
  <text class="script pink" x="660" y="672" font-size="16" textLength="71" lengthAdjust="spacingAndGlyphs">anything</text>
</svg>
</body>
</html>
```